Business Card

Just need business logo with phone number on it. 0472 318 506
And the following on the bottom of the card.

"Your local plumbing experts".
and emblems for card card, cheque and cash

```html
<!DOCTYPE html>
<html lang="en">
<head>
<meta charset="utf-8">
<title>Ridgeline Plumbing &amp; Drainage – Business Card</title>
<link rel="stylesheet" href="https://fonts.googleapis.com/css2?family=Rubik:wght@500;700&display=swap">
<style>
  :root {
    --card-white: #f4f5f3;
    --brand-red: #df2f3c;
    --brand-blue: #3d9bd7;
    --band-text: #ffffff;
  }
  html, body {
    margin: 0;
    padding: 0;
    width: 1200px;
    height: 681px;
    overflow: hidden;
    background: var(--card-white);
  }
  .card {
    position: relative;
    width: 1200px;
    height: 681px;
    background: var(--card-white);
    font-family: "Rubik", sans-serif;
  }
  .brand {
    position: absolute;
    left: 400px;
    top: 110px;
    display: flex;
    align-items: center;
    gap: 22px;
  }
  .brand-mark {
    width: 70px;
    height: 70px;
    background: var(--brand-blue);
    flex: none;
  }
  .brand-name {
    margin: 0;
    color: var(--brand-red);
    font-weight: 700;
    font-size: 54px;
    line-height: 1;
    letter-spacing: 1px;
    text-transform: uppercase;
  }
  .brand-name span {
    display: block;
    font-size: 33px;
    margin-top: 8px;
    letter-spacing: 2px;
  }
  .phone {
    position: absolute;
    left: 400px;
    top: 300px;
    margin: 0;
    color: var(--brand-red);
    font-weight: 700;
    font-size: 64px;
    line-height: 1;
    letter-spacing: 2px;
  }
  .band {
    position: absolute;
    left: 0;
    right: 0;
    bottom: 0;
    height: 235px;
    background: var(--brand-blue);
    display: flex;
    align-items: center;
    justify-content: space-between;
    padding: 0 70px 0 60px;
    box-sizing: border-box;
  }
  .tagline {
    margin: 0;
    color: var(--band-text);
    font-weight: 500;
    font-size: 42px;
    white-space: nowrap;
  }
  .payment-methods {
    display: flex;
    gap: 30px;
  }
  .payment-methods figure { margin: 0; }
  .payment-methods svg { display: block; width: 78px; height: 60px; }
</style>
</head>
<body>
<main class="card">
  <div class="brand">
    <div class="brand-mark" aria-hidden="true"></div>
    <h1 class="brand-name">Ridgeline<span>Plumbing &amp; Drainage</span></h1>
  </div>
  <p class="phone">0472 318 506</p>

  <footer class="band">
    <p class="tagline">Your local plumbing experts</p>
    <div class="payment-methods">
      <figure aria-label="Card payments accepted">
        <svg viewBox="0 0 78 60" fill="none" stroke="#fff" stroke-width="4" stroke-linejoin="round">
          <rect x="6" y="12" width="60" height="38" rx="4"/>
          <line x1="6" y1="24" x2="66" y2="24"/>
          <line x1="14" y1="40" x2="32" y2="40"/>
        </svg>
      </figure>
      <figure aria-label="Cheque accepted">
        <svg viewBox="0 0 78 60" fill="none" stroke="#fff" stroke-width="4" stroke-linejoin="round" stroke-linecap="round">
          <rect x="4" y="14" width="62" height="36" rx="3"/>
          <line x1="12" y1="26" x2="34" y2="26"/>
          <line x1="12" y1="38" x2="28" y2="38"/>
          <path d="M40 40 L70 8"/>
          <path d="M38 44 l2 -6 4 4z" fill="#fff"/>
        </svg>
      </figure>
      <figure aria-label="Cash accepted">
        <svg viewBox="0 0 78 60" fill="none" stroke="#fff" stroke-width="4" stroke-linejoin="round">
          <rect x="6" y="14" width="62" height="34" rx="3"/>
          <circle cx="37" cy="31" r="9"/>
          <circle cx="16" cy="31" r="2" fill="#fff"/>
          <circle cx="58" cy="31" r="2" fill="#fff"/>
        </svg>
      </figure>
    </div>
  </footer>
</main>
</body>
</html>
```